Redesign a Tri-Fold Business Brochure

The attached brochure is poorly designed and has old information. You will notice the attached brochure has only one side. So the other side needs to be created.

The cover and entire brochure should be creatively designed and be pleasing to the eyes. The back of brochure (outside) should have one panel the cover and other two panels the product. The inside of brochure should still be 1. Opportunity 2. Compensation 3. Business Ownership.

The Other PDF attached has updated information and can be used to fill in the old info from the Bad Brochure. IT IS OK TO COPY AND PASTE ONLY A FEW ELEMENTS. MOST OF BROCHURE SHOULD BE RECREATED! THANKS!!

On the other PDF:

Pages 6 & 7 show products (these should go on the outside of brochure that you create)

Page 10 "The Opportunity" section square should be added to the Opportunity Panel on inside part of brochure.

Pages 11 & 12 shows the updated "Compensation" panel info

Page 13 shows the updated "Business Ownership" panel information

I will work with the winner to fill any any missing details. MY MAIN CONCERN IS A GREAT DESIGN!

```html
<!DOCTYPE html>
<html lang="en">
<head>
<meta charset="utf-8">
<title>Novara Tri-Fold Brochure</title>
<link rel="stylesheet" href="https://fonts.googleapis.com/css2?family=Oswald:wght@400;500;600;700&family=Open+Sans:wght@400;600;700&display=swap">
<style>
  :root{
    --stage:#2b2e34;
    --navy:#1c2430;
    --navy-2:#243040;
    --orange:#f28a1e;
    --white:#ffffff;
    --paper:#f1f2f4;
    --ink:#1d2633;
    --muted:#c9d0da;
    --brand-blue:#2f6fc4;
    --sky-top:#7cc3ea;
    --sky-bottom:#2f9fd1;
    --sea:#4cc3c6;
    --sand:#d8cdbd;
  }
  *{box-sizing:border-box;margin:0;padding:0}
  html,body{width:1200px;height:800px;overflow:hidden;background:var(--stage)}
  body{position:relative;font-family:"Open Sans",Arial,sans-serif;color:var(--white)}

  .spread{position:absolute;top:184px;width:840px;height:640px;transform:scale(.675);transform-origin:0 0}
  .spread-outside{left:22px}
  .spread-inside{left:611px}
  .panel{position:absolute;top:0;width:280px;height:640px;overflow:hidden}
  .p1{left:0}.p2{left:280px}.p3{left:560px}
  .head{font-family:"Oswald",Arial,sans-serif;text-transform:uppercase;line-height:1}
  .dark{background:var(--navy)}
  .dark-2{background:var(--navy-2)}

  /* products */
  .panel-title{font-size:26px;font-weight:600;padding:26px 20px 0;color:var(--white)}
  .lead{color:var(--orange);font-size:12px;line-height:1.35;padding:12px 20px 0}
  .product{margin:16px 20px 0}
  .product-photo{height:118px;background:linear-gradient(135deg,var(--sea),var(--sky-bottom) 60%,var(--navy-2))}
  .product-photo.dining{background:linear-gradient(135deg,#8a5a33,#c98a4a 55%,#3a2a22)}
  .product-photo.agent{background:linear-gradient(135deg,#5e7fa3,#9fb7cf 55%,#2c3e55)}
  .product-name{font-family:"Oswald",Arial,sans-serif;font-size:17px;font-weight:600;text-transform:uppercase;color:var(--white);margin-top:10px}
  .product-text{font-size:11.5px;line-height:1.45;color:var(--muted);margin-top:4px}
  .ticks{list-style:none;margin-top:8px}
  .ticks li{display:flex;align-items:center;gap:8px;font-size:11.5px;line-height:1.9;color:var(--white)}
  .ticks svg{flex:none}
  .band{position:absolute;left:0;right:0;bottom:0;background:var(--orange);color:var(--navy);padding:16px 20px;font-family:"Oswald",Arial,sans-serif;font-weight:700;font-size:20px;text-transform:uppercase;text-align:center}

  /* cover */
  .cover{background:linear-gradient(180deg,var(--sky-top),var(--sky-bottom) 55%,var(--sea) 68%,var(--sand) 80%,#bfb3a3)}
  .cover .photo{position:absolute;inset:0}
  .cover .brand{position:absolute;left:22px;top:26px;display:flex;align-items:center;gap:8px}
  .cover .brand .dot{width:26px;height:26px;border-radius:50%;background:var(--brand-blue)}
  .cover .brand span{font-family:"Oswald",Arial,sans-serif;font-weight:700;font-size:30px;color:var(--brand-blue);letter-spacing:1px}
  .cover .tag{position:absolute;left:22px;top:90px}
  .cover .tag .l1{font-size:30px;font-weight:700;color:var(--navy)}
  .cover .tag .l2{font-size:62px;font-weight:700;color:var(--orange);margin-top:4px}
  .cover .tag .l3{font-size:88px;font-weight:700;color:var(--orange);margin-top:2px}
  .cover .foot{position:absolute;right:22px;bottom:24px;font-family:"Oswald",Arial,sans-serif;font-weight:500;font-size:22px;letter-spacing:2px;color:var(--white)}

  /* opportunity */
  .rank{padding:14px 20px 0;font-family:"Oswald",Arial,sans-serif;font-size:16px;font-weight:600;line-height:1.2}
  .rank b{color:var(--orange)}
  .chart{display:block;margin:8px 20px 0}
  .quote{margin:14px 20px 0;background:var(--orange);color:var(--navy);padding:12px 14px;font-size:12px;font-weight:700;line-height:1.35;text-transform:uppercase}
  .quote cite{display:block;text-align:right;font-style:normal;font-size:10px;margin-top:6px}
  .sub-title{font-size:22px;font-weight:600;padding:22px 20px 0}
  .body{font-size:11.5px;line-height:1.5;padding:8px 20px 0;color:var(--muted)}

  /* compensation */
  .sub{font-family:"Oswald",Arial,sans-serif;font-size:14px;font-weight:600;color:var(--orange);text-align:center;text-transform:uppercase;letter-spacing:.5px}
  .sub.white{color:var(--white)}
  .note{font-size:10.5px;text-align:center;line-height:1.35;padding:4px 18px 0;color:#e4e8ee}
  .levels{display:flex;padding:6px 14px 0}
  .levels ul{list-style:none;font-family:"Oswald",Arial,sans-serif;font-size:11.5px;line-height:16px;width:52px}
  .examples{padding:10px 14px 0}
  .eq{font-family:"Oswald",Arial,sans-serif;font-weight:700;font-size:22px;display:flex;justify-content:space-between;align-items:baseline;margin-top:8px}
  .eq em{font-style:normal;color:var(--orange);font-size:26px}
  .eq-labels{display:flex;justify-content:space-between;font-size:7.5px;color:#aeb7c4;text-transform:uppercase;letter-spacing:.5px}

  /* ownership */
  .ownership{background:var(--paper);color:var(--ink)}
  .ownership .panel-title{color:var(--ink);font-size:25px;font-weight:700;padding:24px 18px 0}
  .tier{margin:12px 14px 0;background:var(--white)}
  .tier-bar{display:flex;align-items:center;justify-content:space-between;background:var(--navy);padding:6px 10px;color:var(--white)}
  .tier-name{display:flex;align-items:center;gap:6px;font-family:"Oswald",Arial,sans-serif;font-size:13px;font-weight:600;text-transform:uppercase;line-height:1}
  .tier-name i{width:12px;height:12px;background:var(--orange);border-radius:2px;display:block}
  .price{font-family:"Oswald",Arial,sans-serif;text-align:right;line-height:1}
  .price strong{display:block;font-size:17px}
  .price small{font-size:8.5px;color:var(--orange)}
  .tier ul{list-style:none;padding:6px 10px 8px;font-size:10px;line-height:1.38;text-align:center}
  .tier ul .inc{font-family:"Oswald",Arial,sans-serif;color:var(--orange);font-weight:600;font-size:12px}
  .tier ul b{font-weight:700}
  .slogan{position:absolute;left:0;right:0;bottom:22px;text-align:center;font-family:"Oswald",Arial,sans-serif;font-weight:700;font-size:28px;color:var(--ink)}
  .slogan span{color:var(--orange)}
</style>
</head>
<body>

<!-- outside of the brochure -->
<div class="spread spread-outside">

  <section class="panel p1 dark products">
    <h2 class="head panel-title">The Products</h2>
    <p class="lead">Travel more, spend less and share the savings with everyone you know.</p>
    <article class="product">
      <div class="product-photo" role="img" aria-label="Photograph of a tropical resort by the sea"></div>
      <h3 class="product-name">Travel Club Membership</h3>
      <p class="product-text">Wholesale rates on hotels, resorts, cruises and car rentals around the world.</p>
    </article>
    <article class="product">
      <div class="product-photo dining" role="img" aria-label="Photograph of a restaurant table set for dinner"></div>
      <h3 class="product-name">Concierge &amp; Dining</h3>
      <p class="product-text">A personal concierge to plan every trip, plus restaurant discounts at home.</p>
    </article>
  </section>

  <section class="panel p2 dark-2 products">
    <h2 class="head panel-title">Travel Agent Program</h2>
    <p class="lead">Turn your love of travel into a home-based travel business.</p>
    <article class="product">
      <div class="product-photo agent" role="img" aria-label="Photograph of a travel agent working on a laptop"></div>
      <h3 class="product-name">Member Benefits</h3>
      <ul class="ticks">
        <li><svg width="14" height="14" viewBox="0 0 14 14" aria-hidden="true"><circle cx="7" cy="7" r="7" fill="#f28a1e"/><path d="M3.8 7.2l2.2 2.2 4.2-4.4" stroke="#1c2430" stroke-width="1.8" fill="none"/></svg>Up to 80% commission on travel</li>
        <li><svg width="14" height="14" viewBox="0 0 14 14" aria-hidden="true"><circle cx="7" cy="7" r="7" fill="#f28a1e"/><path d="M3.8 7.2l2.2 2.2 4.2-4.4" stroke="#1c2430" stroke-width="1.8" fill="none"/></svg>Training &amp; certification</li>
        <li><svg width="14" height="14" viewBox="0 0 14 14" aria-hidden="true"><circle cx="7" cy="7" r="7" fill="#f28a1e"/><path d="M3.8 7.2l2.2 2.2 4.2-4.4" stroke="#1c2430" stroke-width="1.8" fill="none"/></svg>Personal mentoring</li>
        <li><svg width="14" height="14" viewBox="0 0 14 14" aria-hidden="true"><circle cx="7" cy="7" r="7" fill="#f28a1e"/><path d="M3.8 7.2l2.2 2.2 4.2-4.4" stroke="#1c2430" stroke-width="1.8" fill="none"/></svg>Timeshare owner benefits</li>
        <li><svg width="14" height="14" viewBox="0 0 14 14" aria-hidden="true"><circle cx="7" cy="7" r="7" fill="#f28a1e"/><path d="M3.8 7.2l2.2 2.2 4.2-4.4" stroke="#1c2430" stroke-width="1.8" fill="none"/></svg>Your own partner website</li>
      </ul>
    </article>
    <p class="band">Novara Travel</p>
  </section>

  <section class="panel p3 cover" aria-label="Brochure cover">
    <div class="photo" role="img" aria-label="Photograph of a couple walking together on a sunny tropical beach"></div>
    <div class="brand"><div class="dot"></div><span>NOVARA</span></div>
    <div class="tag head">
      <div class="l1">Imagine Life</div>
      <div class="l2">Without</div>
      <div class="l3">Limits</div>
    </div>
    <div class="foot">NOVARA TRAVEL</div>
  </section>
</div>

<!-- inside of the brochure -->
<div class="spread spread-inside">

  <section class="panel p1 dark opportunity">
    <h2 class="head panel-title">The Opportunity</h2>
    <p class="lead">More millionaires created from Direct Sales than from any other industry.</p>
    <p class="rank"><b>#84</b> IN WORLD<br><b>#45</b> IN NORTH AMERICA</p>
    <svg class="chart" width="240" height="110" viewBox="0 0 240 110" role="img" aria-label="Bar chart comparing industry revenue">
      <g fill="#f28a1e">
        <rect x="4" y="78" width="46" height="14"/>
        <rect x="64" y="64" width="46" height="28"/>
        <rect x="124" y="50" width="46" height="42"/>
        <rect x="184" y="6" width="46" height="86"/>
      </g>
      <g font-family="Oswald, Arial, sans-serif" font-size="10" fill="#1c2430" text-anchor="middle" font-weight="600">
        <text x="27" y="89">$9 B</text>
        <text x="87" y="82">$11 B</text>
        <text x="147" y="75">$17 B</text>
        <text x="207" y="54">$182 B</text>
      </g>
      <g font-family="Oswald, Arial, sans-serif" font-size="10" fill="#ffffff" text-anchor="middle">
        <text x="27" y="106">Sports</text>
        <text x="87" y="106">Movies</text>
        <text x="147" y="106">Music</text>
        <text x="207" y="106">Direct Sales</text>
      </g>
    </svg>
    <blockquote class="quote">If I had to start all over again, I would choose direct sales and build it.
      <cite>— J. Morrow</cite></blockquote>
    <h3 class="head sub-title">The Opportunity</h3>
    <p class="body">Travel is a trillion dollar industry. Share savings you already love, help others do the same and build a business on your own terms.</p>
  </section>

  <section class="panel p2 dark-2 compensation">
    <h2 class="head panel-title">The Compensation</h2>
    <p class="sub" style="margin-top:8px">Fast Start Bonus</p>
    <p class="note">There is NO LIMIT to how many people you can refer or how much you can earn in FAST START BONUSES!</p>
    <svg width="280" height="86" viewBox="0 0 280 86" role="img" aria-label="Referral bonus diagram">
      <g fill="#f28a1e">
        <circle cx="140" cy="14" r="11"/>
        <circle cx="28" cy="58" r="11"/>
        <circle cx="84" cy="58" r="11"/>
        <circle cx="140" cy="58" r="11"/>
        <circle cx="196" cy="58" r="11"/>
        <circle cx="252" cy="58" r="11"/>
      </g>
      <g fill="#ffffff" font-family="Oswald, Arial, sans-serif" font-size="14" text-anchor="middle">
        <text x="56" y="63">+</text><text x="112" y="63">+</text><text x="168" y="63">+</text><text x="224" y="63">+</text>
      </g>
      <text x="140" y="17" fill="#1c2430" font-family="Oswald, Arial, sans-serif" font-size="7" text-anchor="middle">YOU</text>
      <g fill="#aeb7c4" font-family="Open Sans, Arial, sans-serif" font-size="6.5" text-anchor="middle">
        <text x="28" y="80">$50 BONUS</text><text x="84" y="80">$50 BONUS</text><text x="140" y="80">$50 BONUS</text><text x="196" y="80">$50 BONUS</text><text x="252" y="80">$50 BONUS</text>
      </g>
    </svg>
    <p class="sub white">Residual Income</p>
    <div class="levels">
      <ul>
        <li>L1 - 20%</li><li>L2 - 10%</li><li>L3 - 10%</li><li>L4 - 5%</li><li>L5 - 5%</li><li>L6 - 5%</li><li>L7 - 5%</li><li>L8 - 5%</li><li>L9 - 5%</li>
      </ul>
      <svg width="196" height="144" viewBox="0 0 196 144" role="img" aria-label="Nine level residual income grid">
        <g stroke="#ffffff" stroke-width="1">
          <line x1="0" y1="8" x2="186" y2="8"/><line x1="0" y1="24" x2="186" y2="24"/><line x1="0" y1="40" x2="186" y2="40"/>
          <line x1="0" y1="56" x2="186" y2="56"/><line x1="0" y1="72" x2="186" y2="72"/><line x1="0" y1="88" x2="186" y2="88"/>
          <line x1="0" y1="104" x2="186" y2="104"/><line x1="0" y1="120" x2="186" y2="120"/><line x1="0" y1="136" x2="186" y2="136"/>
          <line x1="30" y1="0" x2="30" y2="140"/><line x1="80" y1="0" x2="80" y2="140"/><line x1="130" y1="0" x2="130" y2="140"/><line x1="175" y1="0" x2="175" y2="140"/>
        </g>
        <g fill="#ffffff">
          <path d="M186 4 L194 8 L186 12Z"/><path d="M186 20 L194 24 L186 28Z"/><path d="M186 36 L194 40 L186 44Z"/>
          <path d="M186 52 L194 56 L186 60Z"/><path d="M186 68 L194 72 L186 76Z"/><path d="M186 84 L194 88 L186 92Z"/>
          <path d="M186 100 L194 104 L186 108Z"/><path d="M186 116 L194 120 L186 124Z"/><path d="M186 132 L194 136 L186 140Z"/>
        </g>
        <g fill="#f28a1e">
          <rect x="90" y="2" width="56" height="12" rx="2"/>
          <rect x="40" y="50" width="62" height="12" rx="2"/>
          <rect x="110" y="98" width="56" height="12" rx="2"/>
          <circle cx="30" cy="24" r="6"/><circle cx="80" cy="24" r="6"/><circle cx="130" cy="40" r="6"/>
          <circle cx="30" cy="72" r="6"/><circle cx="175" cy="72" r="6"/><circle cx="80" cy="88" r="6"/>
          <circle cx="30" cy="120" r="6"/><circle cx="130" cy="136" r="6"/><circle cx="175" cy="24" r="6"/>
        </g>
        <g fill="#1c2430" font-family="Oswald, Arial, sans-serif" font-size="7" text-anchor="middle">
          <text x="118" y="11">UNLIMITED</text><text x="71" y="59">UNLIMITED</text><text x="138" y="107">UNLIMITED</text>
        </g>
      </svg>
    </div>
    <p class="sub" style="margin-top:6px">Residual Income Example</p>
    <div class="examples">
      <div class="eq"><span>10 × 10 × $1 =</span><em>$200</em></div>
      <div class="eq-labels"><span>Members</span><span>Monthly Income</span></div>
      <div class="eq"><span>100 × 10 × $1 =</span><em>$2,000</em></div>
      <div class="eq-labels"><span>Members</span><span>Monthly Income</span></div>
      <div class="eq"><span>1000 × 10 × $1 =</span><em>$20,000</em></div>
      <div class="eq-labels"><span>Members</span><span>Monthly Income</span></div>
    </div>
  </section>

  <section class="panel p3 ownership">
    <h2 class="head panel-title">Business Ownership</h2>

    <article class="tier">
      <div class="tier-bar">
        <div class="tier-name"><i></i>Private<br>Club Member</div>
        <div class="price"><strong>$149.95</strong><small>$49.95 / MONTH</small></div>
      </div>
      <ul>
        <li class="inc">INCLUDES:</li>
        <li>Basic Travel Club Membership</li>
        <li><b>50% Wholesale savings</b></li>
        <li>Access to Organization Program</li>
        <li>Sales &amp; Marketing Management Platform</li>
        <li>Partner Website</li>
        <li>Earn Unlimited Income</li>
      </ul>
    </article>

    <article class="tier">
      <div class="tier-bar">
        <div class="tier-name"><i></i>Elite<br>Club Member</div>
        <div class="price"><strong>$199.95</strong><small>$69.95 / MONTH</small></div>
      </div>
      <ul>
        <li class="inc">INCLUDES:</li>
        <li>Elite Travel Club Membership</li>
        <li><b>100% Wholesale savings</b></li>
        <li>Access to Organization Program</li>
        <li>Sales &amp; Marketing Management Platform</li>
        <li>Partner Website · Earn Unlimited Income</li>
        <li>Personal Concierge · Restaurant Discounts</li>
        <li>Timeshare Owner Benefits</li>
      </ul>
    </article>

    <article class="tier">
      <div class="tier-bar">
        <div class="tier-name"><i></i>Pro<br>Club Member</div>
        <div class="price"><strong>$249.95</strong><small>$89.95 / MONTH</small></div>
      </div>
      <ul>
        <li class="inc">INCLUDES:</li>
        <li>Elite Travel Club Membership</li>
        <li><b>100% Wholesale savings</b></li>
        <li><b>Up To 80% Commission on Travel</b></li>
        <li>Travel Agent Training &amp; Certification</li>
        <li>Personal Mentoring</li>
      </ul>
    </article>

    <p class="slogan">EASY. SIMPLE. <span>FUN.</span></p>
  </section>
</div>

</body>
</html>
```